Lifestyle brand needs lip balm label design

We need a label design for lip balm tubes. The name of our company is "quorvalent"

Design Description:
Our lip balm tubes will be black. The label itself will be clear/transparent. We would like to create a gradient effect with the color green (same shade as our logo) starting from the bottom and slowly fading out to clear so that the black tube is visible (example of gradient shown in attached image)

We have two lip balm flavors: mint and lemongrass.
We would like the top/clear portion of the label to say "MINT" (all caps) . The second label should say "LEMONGRASS" (all caps) in the same location. Our logo "quorvalent" should be in the bottom/green portion of the label. Below the logo, we would like the words "NATURAL BALM" (all caps) in white text

```html
<!DOCTYPE html>
<html lang="en">
<head>
<meta charset="utf-8">
<title>quorvalent – Mint Natural Balm Label</title>
<link rel="stylesheet" href="https://fonts.googleapis.com/css2?family=Jost:wght@300;400;500;700&family=Tinos&display=swap">
<style>
  :root {
    --page-bg: #ffffff;
    --label-top: #0b0e0b;
    --label-mid: #2f4f33;
    --label-bottom: #558c50;
    --flavor-text: #f2f2f2;
    --brand-text: #d9e2d6;
    --tagline-text: #ffffff;
    --size-text: #ffffff;
    --leaf-light: #7ccf4e;
    --leaf-dark: #3f8f2a;
  }
  * { margin: 0; padding: 0; box-sizing: border-box; }
  html, body {
    width: 1200px;
    height: 1000px;
    overflow: hidden;
    background: var(--page-bg);
  }
  .canvas {
    position: relative;
    width: 1200px;
    height: 1000px;
  }
  .balm-label {
    position: absolute;
    left: 483px;
    top: 275px;
    width: 207px;
    height: 690px;
    background: linear-gradient(to bottom,
      var(--label-top) 0%,
      var(--label-top) 6%,
      var(--label-mid) 40%,
      var(--label-bottom) 100%);
    text-align: center;
  }
  .flavor-name {
    position: absolute;
    top: 118px;
    left: 0;
    width: 100%;
    font-family: "Jost", sans-serif;
    font-weight: 500;
    font-size: 66px;
    letter-spacing: 1px;
    line-height: 1;
    color: var(--flavor-text);
  }
  .flavor-art {
    position: absolute;
    top: 220px;
    left: 27px;
    width: 155px;
    height: 135px;
    border-radius: 45%;
    background: radial-gradient(ellipse at center, var(--leaf-light) 0%, var(--leaf-dark) 60%, rgba(63,143,42,0) 72%);
  }
  .brand-name {
    position: absolute;
    top: 459px;
    left: 0;
    width: 100%;
    font-family: "Jost", sans-serif;
    font-weight: 300;
    font-size: 28px;
    line-height: 1.2;
    color: var(--brand-text);
  }
  .product-type {
    position: absolute;
    top: 538px;
    left: 0;
    width: 100%;
    font-family: "Jost", sans-serif;
    font-weight: 400;
    font-size: 20px;
    line-height: 1.2;
    color: var(--tagline-text);
  }
  .net-weight {
    position: absolute;
    top: 578px;
    left: 0;
    width: 100%;
    font-family: "Tinos", serif;
    font-size: 14px;
    line-height: 1.2;
    color: var(--size-text);
  }
</style>
</head>
<body>
  <main class="canvas">
    <section class="balm-label">
      <h1 class="flavor-name">MINT</h1>
      <div class="flavor-art" role="img" aria-label="Sprig of fresh green mint leaves"></div>
      <p class="brand-name">quorvalent</p>
      <p class="product-type">NATURAL BALM</p>
      <p class="net-weight">15 oz&nbsp; 4.2g</p>
    </section>
  </main>
</body>
</html>
```